"Recently Leased" flyer for real estate agency

Looking to have a Recently Leased flyer designed. This will be delivered to apartments and houses closely situated to a property we have recently leased. The idea is to get the attention of owner/landlords in the area that may be considering leasing their property in the future and inform them of the great work we are doing locally. I would like the design to be a two sided flyer using the photoshop (PSD) template below (we would like to be able to edit this once complete should we need to update copy etc in the future). I would like the front page to look like our "for lease sign with the leased sticker on it and copy, I dont want it to look like a typical junk mail flyer.

Target Market(s)

Property owners and investors, male and female aged 28-70

Industry/Entity Type

Real Estate

Font styles to use
Sans Serif

Colors

Designer to choose colors to be used in the design.

Requirements
Must have
• Harbor Keystone Logo
• Contact information
• Copy supplied
Nice to have
• Slick, clean design,
Should not have
• too many colours or too busy a design.
• NO PROPERTY PHOTOS ON FRONT - I want this to be generic and not relate to a specific property image which might confuse people.

```html
<!DOCTYPE html>
<html lang="en">
<head>
<meta charset="utf-8">
<title>Harbor Keystone – Recently Leased Flyer</title>
<link href="https://fonts.googleapis.com/css2?family=Ubuntu:wght@300;400;500;700&display=swap" rel="stylesheet">
<style>
  :root {
    --teal: #2a7e8e;
    --teal-dark: #1f6a78;
    --red: #c3262e;
    --ink: #2b2b2b;
    --grey: #555b5e;
    --paper: #ffffff;
    --backdrop: #e6e7e8;
  }
  * { box-sizing: border-box; margin: 0; padding: 0; }
  html, body { width: 1200px; height: 1200px; overflow: hidden; }
  body {
    background: var(--backdrop);
    font-family: "Ubuntu", sans-serif;
    color: var(--grey);
    position: relative;
  }
  .flyer {
    position: absolute;
    top: 97px;
    width: 463px;
    height: 1007px;
    background: var(--paper);
    box-shadow: 0 6px 18px rgba(0,0,0,.18);
    overflow: hidden;
  }
  .flyer--front { left: 100px; }
  .flyer--back { left: 638px; }

  /* front hero */
  .hero {
    position: absolute; left: 0; top: 0; width: 463px; height: 379px;
    background: linear-gradient(180deg, #8fc8ea 0%, #cfe6f3 38%, #a9b6b6 55%, #5f8a4a 75%, #3f6a35 100%);
  }
  .brand {
    position: absolute; left: 0; top: 56px; width: 463px;
    display: flex; justify-content: center; align-items: center; gap: 8px;
    font-weight: 500; font-size: 26px; color: #1e1e1e; letter-spacing: .3px;
  }
  .brand__mark { width: 12px; height: 12px; background: var(--teal); }

  .headline { position: absolute; left: 28px; top: 394px; right: 20px; }
  .headline__title { font-size: 31px; font-weight: 700; color: var(--teal); line-height: 1.1; }
  .headline__title .accent { color: var(--red); }
  .headline__sub { font-size: 24px; font-weight: 400; color: var(--grey); line-height: 1.3; }
  .headline__teal { font-size: 24px; font-weight: 300; color: var(--teal); line-height: 1.3; margin-top: 2px; }
  .headline__bold { font-size: 24px; font-weight: 700; color: var(--grey); line-height: 1.3; }

  .band {
    position: absolute; left: 0; width: 463px;
    background: var(--teal); color: #fff;
    padding: 16px 28px 0 28px;
  }
  .band--front { top: 527px; height: 252px; }
  .band--back { top: 443px; height: 336px; padding-top: 14px; }
  .band__intro { font-size: 13.6px; font-weight: 700; line-height: 1.35; margin-bottom: 12px; }
  .band--back .band__intro { margin-bottom: 20px; }
  .points { list-style: none; }
  .points li {
    position: relative; padding-left: 18px;
    font-size: 12.8px; font-weight: 300; line-height: 1.35; margin-bottom: 6px;
  }
  .band--back .points li { text-align: justify; margin-bottom: 8px; }
  .points li::before { content: "»"; position: absolute; left: 0; top: -2px; font-size: 15px; font-weight: 500; }

  /* contact block */
  .contact-bar {
    position: absolute; left: 0; top: 869px; width: 463px; height: 51px;
    background: var(--teal); color: #fff; padding: 8px 0 0 137px;
  }
  .contact-bar__name { font-size: 19px; font-weight: 700; line-height: 1; }
  .contact-bar__role { font-size: 14.5px; font-weight: 300; margin-top: 3px; }
  .portrait {
    position: absolute; left: 28px; top: 798px; width: 93px; height: 106px;
    background: var(--teal); padding: 4px;
  }
  .portrait__fill {
    width: 100%; height: 100%; border: 2px solid #fff;
    background: linear-gradient(180deg, #9db4c4 0%, #b49a84 55%, #8fa6c0 100%);
  }
  .contact-copy { position: absolute; left: 138px; top: 796px; right: 28px; }
  .contact-copy__title { font-size: 14.5px; font-weight: 700; color: var(--teal); }
  .contact-copy__text { font-size: 11.6px; font-weight: 300; color: var(--ink); line-height: 1.4; text-align: justify; }
  .flyer--back .contact-copy { top: 797px; }

  .footer { position: absolute; left: 0; top: 936px; width: 463px; height: 56px; font-size: 11.8px; color: var(--ink); }
  .footer__col { position: absolute; top: 0; line-height: 1.36; }
  .footer__col--office { left: 28px; padding-left: 19px; }
  .footer__col--reach { left: 222px; }
  .footer__divider { position: absolute; left: 206px; top: 2px; width: 1px; height: 50px; background: #9a9a9a; }
  .footer strong { font-weight: 500; }
  .footer__light { font-weight: 300; }
  .footer .row { display: flex; align-items: center; gap: 5px; }
  .icon { width: 10px; height: 10px; fill: var(--teal); flex: none; }
  .icon--home { position: absolute; left: 0; top: 2px; width: 13px; height: 12px; }

  /* back gallery */
  .photo {
    position: absolute; box-shadow: 0 2px 4px rgba(0,0,0,.3); overflow: hidden;
    border: 1px solid #ddd;
  }
  .photo--main { left: 29px; top: 29px; width: 406px; height: 264px;
    background: linear-gradient(120deg, #8fb07a 0%, #5b6770 30%, #c77b55 60%, #4b4f57 100%); }
  .photo--small { top: 307px; width: 128px; height: 120px; }
  .photo--bed { left: 29px; background: linear-gradient(160deg, #d8cfb8 0%, #c9b896 55%, #a67b4a 100%); }
  .photo--living { left: 168px; background: linear-gradient(160deg, #c8ccd0 0%, #6c6c6c 50%, #8b7a66 100%); }
  .photo--kitchen { left: 307px; background: linear-gradient(160deg, #f2f2f0 0%, #d9d9d6 55%, #3a3a3a 100%); }
  .ribbon {
    position: absolute; left: -26px; top: 14px; width: 96px; height: 15px;
    background: var(--red); color: #fff; transform: rotate(-45deg);
    font-size: 8px; font-weight: 500; text-align: center; line-height: 15px; letter-spacing: .3px;
  }
  .photo--small .ribbon { left: -30px; top: 10px; width: 88px; height: 13px; line-height: 13px; font-size: 7px; }
</style>
</head>
<body>

<section class="flyer flyer--front">
  <div class="hero" role="img" aria-label="Row of modern terraced townhouses with landscaped gardens under a blue sky"></div>
  <div class="brand"><span class="brand__mark"></span>HARBOR KEYSTONE</div>

  <div class="headline">
    <h1 class="headline__title">WE RECENTLY <span class="accent">LEASED</span></h1>
    <p class="headline__sub">a property in your building or street.</p>
    <p class="headline__teal">Attracting a great reliable tenant and</p>
    <p class="headline__bold">fantastic return for the owner.</p>
  </div>

  <div class="band band--front">
    <p class="band__intro">We received a high number of enquires and applications for this property and have a database of screened and qualified tenants looking to lease in your area.</p>
    <ul class="points">
      <li>On average we lease properties 2 weeks faster than the Northern Beaches average</li>
      <li>Strong database of tenants actively looking in the area</li>
      <li>All we do is lease property, no sales – so tenanting and managing your property is our priority</li>
      <li>90 day money back guarantee on our level of service</li>
      <li>Highly competitive, simple all-inclusive pricing.</li>
      <li>Experience the difference of a property management specialist</li>
    </ul>
  </div>

  <div class="contact-copy">
    <h2 class="contact-copy__title">CONTACT SAM</h2>
    <p class="contact-copy__text">to get your free rental appraisal or transfer your existing investment to an agency that will give it the attention it deserves and maxamise your return.</p>
  </div>
  <div class="contact-bar">
    <p class="contact-bar__name">SAM CARVER</p>
    <p class="contact-bar__role">Director/Property Manager</p>
  </div>
  <div class="portrait"><div class="portrait__fill" role="img" aria-label="Portrait photo of the property manager"></div></div>

  <div class="footer">
    <div class="footer__col footer__col--office">
      <svg class="icon icon--home" viewBox="0 0 13 12"><path d="M6.5 0 0 5.5h1.8V12h3.4V8h2.6v4h3.4V5.5H13z"/></svg>
      <strong>Harbor Keystone Agency</strong><br>
      <span class="footer__light">Level 2, 18 Harbour Lane,<br>Seaview NSW 2090</span>
    </div>
    <div class="footer__divider"></div>
    <div class="footer__col footer__col--reach">
      <div class="row"><svg class="icon" viewBox="0 0 10 10"><path d="M2 0 3.6 2.4 2.6 3.6c.6 1.4 2.3 3.1 3.8 3.8l1.2-1L10 8l-.6 1.6C8.9 10.4 6 10 3.4 7.2 1 4.6-.4 1.5.4.6z"/></svg><strong>0400 555 019</strong></div>
      <div class="row footer__light"><svg class="icon" viewBox="0 0 10 10"><path d="M0 2h10v7H0zM.6 2.4 5 5.8l4.4-3.4V3L5 6.4.6 3z"/></svg>sam@harborkeystone.example</div>
      <div class="row footer__light"><svg class="icon" viewBox="0 0 10 10"><circle cx="5" cy="5" r="4.5" fill="none" stroke="#2a7e8e" stroke-width="1"/><path d="M.5 5h9M5 .5c-2.4 2.8-2.4 6.2 0 9M5 .5c2.4 2.8 2.4 6.2 0 9" fill="none" stroke="#2a7e8e" stroke-width=".8"/></svg>www.harborkeystone.example</div>
    </div>
  </div>
</section>

<section class="flyer flyer--back">
  <div class="photo photo--main" role="img" aria-label="Leased apartment balcony with glass table, brick wall and louvred screen"><span class="ribbon">LEASED</span></div>
  <div class="photo photo--small photo--bed" role="img" aria-label="Leased apartment bedroom"><span class="ribbon">LEASED</span></div>
  <div class="photo photo--small photo--living" role="img" aria-label="Leased apartment living and dining room"><span class="ribbon">LEASED</span></div>
  <div class="photo photo--small photo--kitchen" role="img" aria-label="Leased apartment kitchen"><span class="ribbon">LEASED</span></div>

  <div class="band band--back">
    <p class="band__intro">The fundamental idea behind Harbor Keystone Agency was to give landlords a simple and confidence inspiring experience. We achieve this through:</p>
    <ul class="points">
      <li>Unique marketing that goes beyond the standard listing sites and has seen our average days-on-market at 5.9days for 2018.</li>
      <li>A simple, yet competitive fee structure.</li>
      <li>Excellent customer service through an experienced professional property manager.</li>
      <li>Sound advice and communication through out the leasing and management process.</li>
      <li>A simple yet powerful landlord portal which enables owners to view media rich inspection reports, financial reports and maintenance progress at anytime.</li>
      <li>We then back our service promise with a 90day money back guarantee.</li>
    </ul>
  </div>

  <div class="contact-copy">
    <p class="contact-copy__text">If you have been considering leasing your property, purchasing a local investment or aren't happy with your current managing agency, please don't hesitate to contact your local rental specialist for more information:</p>
  </div>
  <div class="contact-bar">
    <p class="contact-bar__name">SAM CARVER</p>
    <p class="contact-bar__role">Director/Property Manager</p>
  </div>
  <div class="portrait"><div class="portrait__fill" role="img" aria-label="Portrait photo of the property manager"></div></div>

  <div class="footer">
    <div class="footer__col footer__col--office">
      <svg class="icon icon--home" viewBox="0 0 13 12"><path d="M6.5 0 0 5.5h1.8V12h3.4V8h2.6v4h3.4V5.5H13z"/></svg>
      <strong>Harbor Keystone Agency</strong><br>
      <span class="footer__light">Level 2, 18 Harbour Lane,<br>Seaview NSW 2090</span>
    </div>
    <div class="footer__divider"></div>
    <div class="footer__col footer__col--reach">
      <div class="row"><svg class="icon" viewBox="0 0 10 10"><path d="M2 0 3.6 2.4 2.6 3.6c.6 1.4 2.3 3.1 3.8 3.8l1.2-1L10 8l-.6 1.6C8.9 10.4 6 10 3.4 7.2 1 4.6-.4 1.5.4.6z"/></svg><strong>0400 555 019</strong></div>
      <div class="row footer__light"><svg class="icon" viewBox="0 0 10 10"><path d="M0 2h10v7H0zM.6 2.4 5 5.8l4.4-3.4V3L5 6.4.6 3z"/></svg>sam@harborkeystone.example</div>
      <div class="row footer__light"><svg class="icon" viewBox="0 0 10 10"><circle cx="5" cy="5" r="4.5" fill="none" stroke="#2a7e8e" stroke-width="1"/><path d="M.5 5h9M5 .5c-2.4 2.8-2.4 6.2 0 9M5 .5c2.4 2.8 2.4 6.2 0 9" fill="none" stroke="#2a7e8e" stroke-width=".8"/></svg>www.harborkeystone.example</div>
    </div>
  </div>
</section>

</body>
</html>
```